Business card design for new, innovative company - BoldHarbor

We are a new company looking for a business card design that is fun, different and quirky. Must use corporate colour green - CMYK C:55, M:0, Y:100, K:0, and corporate colour grey - C:0, M:0, Y: 0, K:70.

We have developed the first real time data application, in which people are able to profile the data of their existing customers in order to pull out more good fit clients to direct their marketing activities at.

Industry/Entity Type

Marketing

Requirements
Must have
• Logo, name, title, telephone number, fax number, email, website, address

```html
<!DOCTYPE html>
<html lang="en">
<head>
<meta charset="utf-8">
<title>BoldHarbor – Business Card</title>
<link href="https://fonts.googleapis.com/css2?family=Arimo:wght@400;700&display=swap" rel="stylesheet">
<style>
  :root {
    --brand-green: #7bc142;
    --brand-grey: #6d6e71;
    --paper: #ffffff;
    --backdrop: #e9e7e3;
    --ink: #58595b;
  }
  * { box-sizing: border-box; margin: 0; padding: 0; }
  html, body {
    width: 1200px; height: 900px; overflow: hidden;
    background: var(--backdrop);
    font-family: "Arimo", Arial, sans-serif;
  }
  .stage {
    width: 1200px; height: 900px;
    display: flex; align-items: center; justify-content: center; gap: 110px;
  }
  .card {
    width: 360px; height: 580px; position: relative;
    box-shadow: 0 6px 18px rgba(0,0,0,.12);
    overflow: hidden;
  }
  .card--front { background: var(--paper); }
  .card--back {
    background: var(--brand-green);
    display: flex; align-items: center; justify-content: center;
  }

  .wordmark {
    font-weight: 700; color: var(--brand-grey);
    letter-spacing: -1.5px; white-space: nowrap;
  }
  .card--front .wordmark {
    position: absolute; top: 92px; left: 0; right: 0;
    text-align: center; font-size: 50px;
  }

  .name-band {
    position: absolute; top: 212px; left: 0; right: 0; height: 50px;
    background: var(--brand-green);
    display: flex; align-items: center; justify-content: center;
    color: #fff; font-weight: 700; font-size: 21px; letter-spacing: .3px;
  }

  .contact-list {
    position: absolute; top: 318px; left: 34px; right: 20px;
    list-style: none; color: var(--ink); font-size: 16px; line-height: 1.25;
  }
  .contact-list li {
    display: flex; align-items: flex-start; gap: 10px; margin-bottom: 9px;
  }
  .contact-list svg { flex: 0 0 12px; width: 12px; height: 14px; margin-top: 3px; fill: var(--ink); }

  .emblem {
    width: 300px; height: 300px; border-radius: 50%;
    background: var(--paper);
    display: flex; align-items: center; justify-content: center;
  }
  .emblem .wordmark { font-size: 44px; }
</style>
</head>
<body>
<main class="stage">
  <section class="card card--front" aria-label="Business card front">
    <div class="wordmark">BoldHarbor</div>
    <div class="name-band">Nadia Fenwick</div>
    <ul class="contact-list">
      <li>
        <svg viewBox="0 0 12 14" aria-hidden="true"><path d="M6 0a4.5 4.5 0 0 0-4.5 4.5C1.5 8 6 14 6 14s4.5-6 4.5-9.5A4.5 4.5 0 0 0 6 0zm0 6.3a1.8 1.8 0 1 1 0-3.6 1.8 1.8 0 0 1 0 3.6z"/></svg>
        <span>27 Larkfield Road, Ely,<br>Cambridgeshire, CB7 4QT</span>
      </li>
      <li>
        <svg viewBox="0 0 12 14" aria-hidden="true"><path d="M3 0h6a1.5 1.5 0 0 1 1.5 1.5v11A1.5 1.5 0 0 1 9 14H3a1.5 1.5 0 0 1-1.5-1.5v-11A1.5 1.5 0 0 1 3 0zm0 2v9h6V2zm3 9.6a.8.8 0 1 0 0 1.6.8.8 0 0 0 0-1.6z"/></svg>
        <span>07700900418</span>
      </li>
      <li>
        <svg viewBox="0 0 12 14" aria-hidden="true"><circle cx="6" cy="7" r="6"/><path d="M4 4.2l1 .3.3 1.4-.7.6a4 4 0 0 0 1.9 1.9l.6-.7 1.4.3.3 1-.9.8C5.9 9.6 3.9 7.5 3.3 5.1z" fill="#fff"/></svg>
        <span>01632 960284</span>
      </li>
      <li>
        <svg viewBox="0 0 12 14" aria-hidden="true"><path d="M0 3.5h12v7H0zm1 1v.3l5 3.2 5-3.2v-.3zm0 1.5v3.5h10V6L6 9.1z"/></svg>
        <span>nadia.fenwick@harbordata.com</span>
      </li>
      <li>
        <svg viewBox="0 0 12 14" aria-hidden="true"><circle cx="6" cy="7" r="6"/><path d="M0.5 7h11M6 1v12M2 4h8M2 10h8" stroke="#fff" stroke-width=".8" fill="none"/></svg>
        <span>www.boldharbor.com</span>
      </li>
    </ul>
  </section>

  <section class="card card--back" aria-label="Business card back">
    <div class="emblem">
      <div class="wordmark">BoldHarbor</div>
    </div>
  </section>
</main>
</body>
</html>
```